Ridgeline Wild Craft DL flyer

I'm looking for a new flyer for my startup business. In Darwin Australia.
Aimed at family's and short stay tourists the "Ridgeline Wild Craft" 4 hr tour will give people a basic understanding of some essential bush survival skills in the Australian Outback.
things covered in this 4 hr tour are
1. Finding water.
2. finding food.
3. Finding/making shelter and fire.
4. Finding your way home.

The tour will pick clients up in an air conditioned purpose build 4WD and take them to a nearby bushland area where they will have the opportunity to catch and harvest some native bushtucker.
They will then be able to find/harvest some water for survival situations.
While we cook our bush tucker they will also learn to find their way home through ancient navigation techniques as well.

Clients will then be dropped back to their accomodation with some fun and vital knowledge of surviving in the Australian outback.
At the end of the tour the group will be able to take home a basic survival kit which they will be able to use through the skills they just gained on the tour.

I'd like a two sided DL size flyer emphasising the following points.
4hr/half day tour
Fun for the family
Free survival kit included.
Eat what you catch
Learn essential survival skills
Provided buy an experienced and passionate bushman.
$150/head including transfers.

I'll provide some pictures for the flyer and any extra content you require.

Target Market(s)

Family's
Short stay tourists

Industry/Entity Type

Tourism

Colors

Designer to choose colors to be used in the design.

Requirements
Must have
• As per brief
Nice to have
• Any extra content and flair designers would like to add
Should not have
• Any images which aren't Australian

```html
<!DOCTYPE html>
<html lang="en">
<head>
<meta charset="utf-8">
<title>Ridgeline Wild Craft DL flyer</title>
<link rel="stylesheet" href="https://fonts.googleapis.com/css2?family=Montserrat:wght@400;500&family=Oswald:wght@600;700&display=swap">
<style>
  :root {
    --stage: #111111;
    --paper: #ffffff;
    --title-bg: #f6f6f6;
    --title-grey: #9b9b9b;
    --olive-top: #8c8a1c;
    --olive-bottom: #4b6a12;
    --leaf: #4a7a0f;
    --mist: #ececec;
    --ink: #1a1a1a;
    --bark: #2f291d;
  }
  * { margin: 0; padding: 0; box-sizing: border-box; }
  html, body { width: 1100px; height: 1200px; overflow: hidden; }
  body {
    background: radial-gradient(ellipse at center, #1c1c1c 0%, var(--stage) 70%);
    font-family: "Montserrat", sans-serif;
    position: relative;
  }
  .flyer { position: absolute; top: 198px; width: 377px; height: 800px; }
  .flyer--front { left: 155px; background: var(--paper); }
  .flyer--back { left: 580px; background: var(--mist); }

  .photo { position: absolute; }
  .photo--landscape { left: 6px; top: 5px; width: 365px; height: 171px;
    background: linear-gradient(180deg, #7e9a5c 0%, #6f8c44 50%, #9c6a3a 78%, #8aa04c 100%); }
  .photo--palm { left: 6px; top: 296px; width: 211px; height: 195px;
    background: linear-gradient(160deg, #93ad52 0%, #527d2c 55%, #c8b798 100%); }
  .photo--guide-crab { left: 6px; top: 494px; width: 211px; height: 196px;
    background: linear-gradient(170deg, #5c7b3d 0%, #9a6b4e 55%, #4b4a3b 100%); }
  .photo--guide-portrait { left: 222px; top: 296px; width: 149px; height: 394px;
    background: linear-gradient(180deg, #f1f1ee 0%, #b79b83 45%, #d8d5cb 100%); }

  .title-panel {
    position: absolute; left: 6px; top: 176px; width: 365px; height: 117px;
    background: var(--title-bg);
  }
  .title {
    position: absolute; left: 0; top: 12px; width: 365px;
    text-align: center; font-family: "Oswald", sans-serif; font-weight: 700;
    font-size: 52px; line-height: 46px; color: var(--title-grey); letter-spacing: 1px;
  }

  .cta-band {
    position: absolute; left: 6px; top: 695px; width: 365px; height: 99px;
    background: linear-gradient(180deg, var(--olive-top), var(--olive-bottom));
    color: #fff; text-align: center;
  }
  .cta-band .cta-label { font-size: 29px; font-weight: 500; margin-top: 10px; letter-spacing: 1px; line-height: 34px; }
  .cta-band .cta-phone { font-family: "Oswald", sans-serif; font-weight: 700; font-size: 40px; line-height: 46px; }

  .story {
    position: absolute; left: 0; top: 0; width: 377px; height: 243px;
    background: var(--leaf); color: #fff; padding: 25px 14px 0 17px;
  }
  .story h2 { font-family: "Oswald", sans-serif; font-weight: 600; font-size: 12px; margin-bottom: 9px; letter-spacing: .2px; }
  .story p { font-size: 11.2px; line-height: 14.6px; margin-bottom: 9px; }

  .highlights { position: absolute; left: 58px; top: 258px; list-style: none; color: var(--ink); }
  .highlights li { font-size: 16px; line-height: 20px; position: relative; padding-left: 12px; margin-bottom: 11px; }
  .highlights li::before { content: ""; position: absolute; left: 0; top: 8px; width: 6px; height: 6px; border-radius: 50%; background: var(--ink); }

  .photo--bush-fruit { left: 24px; top: 505px; width: 139px; height: 179px;
    background: linear-gradient(160deg, #a08d70 0%, #7d9f48 50%, #c79b84 100%); }
  .photo--crayfish { left: 173px; top: 505px; width: 177px; height: 119px;
    background: linear-gradient(170deg, #6a5a48 0%, #d1a68d 50%, #5b7a6a 100%); }

  .back-cta { position: absolute; left: 173px; top: 632px; width: 177px; text-align: center; color: var(--ink); }
  .back-cta .cta-label { font-size: 18px; line-height: 22px; letter-spacing: .5px; }
  .back-cta .cta-phone { font-family: "Oswald", sans-serif; font-weight: 700; font-size: 26px; line-height: 32px; }

  .address-band {
    position: absolute; left: 0; top: 694px; width: 377px; height: 106px;
    background: var(--bark); color: #fff; font-size: 15.5px;
    display: flex; align-items: center; justify-content: center;
  }
</style>
</head>
<body>
  <section class="flyer flyer--front">
    <div class="photo photo--landscape" role="img" aria-label="Outback savanna with termite mounds among gum trees"></div>
    <div class="title-panel">
      <h1 class="title">RIDGELINE<br>WILD CRAFT</h1>
    </div>
    <div class="photo photo--palm" role="img" aria-label="Pandanus palm fronds in the bush"></div>
    <div class="photo photo--guide-crab" role="img" aria-label="Bushman holding a mud crab by a creek"></div>
    <div class="photo photo--guide-portrait" role="img" aria-label="Bushman guide in a wide-brim hat"></div>
    <div class="cta-band">
      <p class="cta-label">CALL US TODAY</p>
      <p class="cta-phone">+123 456 7890</p>
    </div>
  </section>

  <section class="flyer flyer--back">
    <div class="story">
      <h2>ABOUT THE TOUR</h2>
      <p>The tour will pick clients up in an air conditioned purpose built 4WD and take them to a nearby bushland area where they will have the opportunity to catch and harvest some native bushtucker. They will then be able to find/harvest some water for survival situations. While we cook our bush tucker they will also learn to find their way home through ancient navigation techniques as well.</p>
      <p>Clients will then be dropped back to their accommodation with some fun and vital knowledge of surviving in the Australian outback. At the end of the tour the group will be able to take home a basic survival kit which they will be able to use through the skills they just gained on the tour.</p>
    </div>
    <ul class="highlights">
      <li>4hr/half day tour</li>
      <li>Fun for the family</li>
      <li>Free survival kit included</li>
      <li>Eat what you catch</li>
      <li>Learn essential survival skills</li>
      <li>Provided by an experienced<br>and passionate bushman</li>
      <li>$150/head including transfers</li>
    </ul>
    <div class="photo photo--bush-fruit" role="img" aria-label="Hand holding green bush fruit pods"></div>
    <div class="photo photo--crayfish" role="img" aria-label="Hands holding a freshwater crayfish"></div>
    <div class="back-cta">
      <p class="cta-label">CALL US TODAY</p>
      <p class="cta-phone">+123 456 7890</p>
    </div>
    <div class="address-band">14 Stuart Highway, Darwin NT 0800</div>
  </section>
</body>
</html>
```